Business card for exciting VC company

Should look simple, crisp, and modern.

Industry/Entity Type

Venture Capital

Contact Information for Business Card

Would like to see at least one design that has our blue on the back with the tagline "Transforming Traditional Industry" and white front with contact details.

Font styles to use
Sans Serif

Requirements
Must have
• Logo

Darius Pellworth
dpellworth@brindlegate.vc
Managing Partner
M (628)304-xxxx

```html
<!DOCTYPE html>
<html lang="en">
<head>
<meta charset="utf-8">
<title>Brindlegate Capital – Business Card</title>
<link rel="stylesheet" href="https://fonts.googleapis.com/css2?family=Lato:wght@400;700&display=swap">
<style>
  :root {
    --backdrop: #9b9b9b;
    --card-white: #ffffff;
    --brand-blue: #4384c5;
    --name-blue: #4585c8;
    --ink: #111111;
    --body-grey: #464646;
    --on-blue: #ffffff;
  }
  * { box-sizing: border-box; margin: 0; padding: 0; }
  html, body {
    width: 1021px;
    height: 1200px;
    overflow: hidden;
  }
  body {
    position: relative;
    background: var(--backdrop);
    font-family: "Lato", sans-serif;
  }
  .card {
    position: absolute;
    width: 753px;
    height: 429px;
  }
  .card--front {
    left: 134px;
    top: 119px;
    background: var(--card-white);
  }
  .card--back {
    left: 131px;
    top: 651px;
    background: var(--brand-blue);
  }
  .wordmark {
    font-family: "Lato", sans-serif;
    font-weight: 700;
    text-transform: uppercase;
    letter-spacing: 0.12em;
    white-space: nowrap;
  }
  .card--front .wordmark {
    position: absolute;
    left: 38px;
    top: 94px;
    font-size: 24px;
    color: var(--ink);
  }
  .contact {
    position: absolute;
    right: 33px;
    top: 268px;
    text-align: right;
    color: var(--body-grey);
  }
  .contact__name {
    font-size: 28px;
    font-weight: 700;
    color: var(--name-blue);
    text-transform: uppercase;
    letter-spacing: -0.01em;
    line-height: 1;
  }
  .contact__title {
    font-size: 20px;
    margin-top: 8px;
    line-height: 1.2;
  }
  .contact__details {
    margin-top: 14px;
    font-size: 20px;
    line-height: 28px;
  }
  .title-rule {
    position: absolute;
    left: 38px;
    top: 313px;
    width: 511px;
    height: 1px;
    background: var(--brand-blue);
  }
  .card--back .wordmark {
    position: absolute;
    left: 0;
    right: 0;
    top: 186px;
    text-align: center;
    font-size: 34px;
    color: var(--on-blue);
  }
  .tagline {
    position: absolute;
    left: 0;
    right: 0;
    top: 375px;
    display: flex;
    align-items: center;
    gap: 8px;
    color: var(--on-blue);
    font-size: 21px;
    white-space: nowrap;
  }
  .tagline::before,
  .tagline::after {
    content: "";
    flex: 1;
    height: 1px;
    background: var(--on-blue);
  }
</style>
</head>
<body>
  <section class="card card--front" aria-label="Business card front">
    <div class="wordmark">Brindlegate Capital</div>
    <div class="title-rule"></div>
    <div class="contact">
      <div class="contact__name">Darius Pellworth</div>
      <div class="contact__title">Managing Partner</div>
      <div class="contact__details">
        <div class="contact__phone">(628)304-xxxx</div>
        <div class="contact__email">dpellworth@brindlegate.vc</div>
      </div>
    </div>
  </section>

  <section class="card card--back" aria-label="Business card back">
    <div class="wordmark">Brindlegate Capital</div>
    <div class="tagline">Transforming Traditional Industries</div>
  </section>
</body>
</html>
```